BrewHarbor coffee packaging design

We need a vector design (AI) for the printing of our coffee bags.

The bags are double sided. Front will be simple with logo and web address. Back will have lots of information (below) and the wording can be changed to suit if required.

Actual bag dimensions are: 240mm wide x 335mm high (each side) artwork should be inside those sizes.

Front:
Requires - BrewHarbor cup logo, web address (brewharbor.com.au) in lowercase Papyrus font and the words BREW HARBOR in uppercase.
**added** The front will also need a 90mm x 35mm no artwork area so we can place a sticker.

Back:
1.
Silver Kettle Logo (needs to be entire unmodified logo) and the tagline of "Overall winner of Australia's biggest coffee roasting competition"

2.
BrewHarbor is a family business, proudly Australian owned and operated. We strive to provide amazing coffee, excellent service and great value to all our customers.

3.
Our coffee is fresh roasted to order and shipped same day.

4.
50c from every kilogram sold goes directly to projects in coffee growing regions. TrueShare is the Kindest Deal of all - see: trueshare.net

Logos are attached and higher resolution ones are available if needed.

Industry/Entity Type

Business

Requirements
Must have
• Per the description, BrewHarbor logo and webaddress on the front and Silver Kettle logo on the back are required.

```html
<!DOCTYPE html>
<html lang="en">
<head>
<meta charset="utf-8">
<title>BrewHarbor coffee bag – back and front</title>
<link rel="stylesheet" href="https://fonts.googleapis.com/css2?family=Macondo&family=Marcellus&display=swap">
<style>
  :root {
    --bag-gold: #c89a3a;
    --ink-brown: #2b1a0c;
    --sheet-white: #ffffff;
    --frame-brown: #5a3410;
    --badge-light: #ece6dc;
    --coin-silver: #9aa3a6;
    --bean-dark: #3a2210;
  }
  * { margin: 0; padding: 0; box-sizing: border-box; }
  html, body {
    width: 1200px; height: 828px; overflow: hidden;
    background: var(--sheet-white);
  }
  .sheet { position: relative; width: 1200px; height: 828px; }
  .bag-side {
    position: absolute; top: 0; height: 828px;
    background: var(--bag-gold); color: var(--ink-brown);
    font-family: "Macondo", "Marcellus", serif;
  }
  .bag-back { left: 0; width: 594px; }
  .bag-front { left: 607px; width: 593px; }
  .centered { position: absolute; left: 0; right: 0; text-align: center; }

  /* back */
  .brand-small {
    top: 66px; font-size: 21px; line-height: 20px; letter-spacing: 0.5px;
  }
  .brand-mark-small {
    position: absolute; left: 262px; top: 112px; width: 72px; height: 72px;
    border: 3px solid var(--ink-brown); border-radius: 50%;
  }
  .web-small { top: 201px; font-size: 12px; font-family: "Marcellus", serif; }
  .award-tagline { top: 258px; font-size: 16px; font-family: "Marcellus", serif; }
  .award-badge {
    position: absolute; left: 233px; top: 295px; width: 128px; height: 126px;
    border: 3px solid var(--frame-brown); padding: 4px;
  }
  .award-badge-inner {
    width: 100%; height: 100%;
    border: 1.5px solid var(--frame-brown);
    background: var(--badge-light);
  }
  .about {
    position: absolute; left: 58px; top: 452px; width: 500px;
    font-family: "Marcellus", serif; font-size: 11px; line-height: 16px;
  }
  .about p { margin-bottom: 23px; }
  .about p.gap-wide { margin-top: 9px; }
  .partner-name { top: 647px; font-size: 21px; }
  .partner-mark {
    position: absolute; left: 262px; top: 680px; width: 64px; height: 64px;
    border-radius: 50%;
    background: radial-gradient(circle at 45% 40%, var(--coin-silver), var(--bean-dark));
  }
  .partner-tagline { top: 766px; font-size: 10px; font-family: "Marcellus", serif; }

  /* front */
  .brand-large { top: 58px; font-size: 84px; line-height: 74px; letter-spacing: 2px; }
  .brand-mark-large {
    position: absolute; left: 152px; top: 235px; width: 290px; height: 290px;
    border: 10px solid var(--ink-brown); border-radius: 50%;
  }
  .web-large { top: 588px; font-size: 40px; }
</style>
</head>
<body>
<main class="sheet">
  <section class="bag-side bag-back">
    <h2 class="centered brand-small">BREW<br>HARBOR</h2>
    <div class="brand-mark-small" aria-hidden="true"></div>
    <p class="centered web-small">brewharbor.com.au</p>
    <p class="centered award-tagline">"Overall winner of Australia's biggest coffee roasting competition"</p>
    <div class="award-badge" role="img" aria-label="Silver Kettle award badge">
      <div class="award-badge-inner"></div>
    </div>
    <div class="about">
      <p>BrewHarbor is a family business, proudly Australian owned and operated. We strive to provide amazing coffee, excellent service and great value to all our customers.</p>
      <p>Our coffee is fresh roasted to order and shipped same day.</p>
      <p>50c from every kilogram sold goes directly to projects in coffee growing regions.</p>
      <p class="gap-wide">TrueShare is the Kindest Deal of all - see: trueshare.net</p>
    </div>
    <h3 class="centered partner-name">TrueShare</h3>
    <div class="partner-mark" role="img" aria-label="TrueShare badge: coin resting on a coffee bean"></div>
    <p class="centered partner-tagline">"giving a little back"</p>
  </section>

  <section class="bag-side bag-front">
    <h1 class="centered brand-large">BREW<br>HARBOR</h1>
    <div class="brand-mark-large" aria-hidden="true"></div>
    <p class="centered web-large">brewharbor.com.au</p>
  </section>
</main>
</body>
</html>
```